Business card for new business - financial management

I need a business card designed for my new business. I'm the owner / sole trader of QVB Consulting, which provides financial management services for Government. I'd like the design to incorporate the attached business name and colours. The design should include colour and not be too way out - it needs to look at home in a government environment.
Details to be included on the card are:
QVB Consulting
Miriam Haskett
0400 386 924
miriamrhaskett@fernmail.example
47 Pallister Crescent, Fernleigh ACT 2699
Single or double sided designs would be good.
Employees at Australian Federal Government agencies
Government

```html
<!DOCTYPE html>
<html lang="en">
<head>
<meta charset="utf-8">
<title>QVB Consulting – Business Card</title>
<link rel="stylesheet" href="https://fonts.googleapis.com/css2?family=Noto+Serif:wght@400;700&display=swap">
<style>
  :root {
    --backdrop: #e4e6ea;
    --card-white: #ffffff;
    --navy: #1d4f9a;
    --royal: #1a56a2;
    --sky: #39a4da;
    --teal: #2b7e94;
    --aqua: #94d4de;
    --aqua-soft: #a8dce6;
  }
  * { box-sizing: border-box; margin: 0; padding: 0; }
  html, body {
    width: 1200px; height: 900px; overflow: hidden;
    background: var(--backdrop);
    font-family: "Noto Serif", Georgia, serif;
  }
  .canvas { position: relative; width: 1200px; height: 900px; }

  .card {
    position: absolute; left: 320px; width: 560px; height: 320px;
    border-radius: 22px; overflow: hidden;
    box-shadow: 0 10px 28px rgba(0,0,0,.18);
  }
  .card-front { top: 90px; background: var(--card-white); }
  .card-back  { top: 480px; background: linear-gradient(135deg, #1b5aa8, #174f98); }

  /* front */
  .front-brand {
    position: absolute; right: 40px; top: 36px;
    font-size: 34px; font-weight: 400; color: var(--teal); letter-spacing: .5px;
    white-space: nowrap;
  }
  .holder { position: absolute; left: 44px; top: 122px; }
  .holder-name { font-size: 30px; font-weight: 400; color: var(--navy); line-height: 1.1; white-space: nowrap; }
  .holder-role { font-size: 19px; color: var(--sky); margin-top: 2px; }

  .contact-list {
    position: absolute; left: 236px; top: 198px; list-style: none;
    font-size: 14px; color: var(--navy);
  }
  .contact-item { display: flex; align-items: flex-start; gap: 10px; margin-bottom: 9px; line-height: 1.3; white-space: nowrap; }
  .contact-icon { flex: none; width: 22px; height: 22px; }

  .edge-band { position: absolute; left: 0; right: 0; bottom: 0; height: 8px; display: flex; }
  .edge-band-light { flex: 1; background: var(--aqua-soft); }
  .edge-band-dark  { flex: 1; background: var(--royal); }

  /* back */
  .back-brand {
    position: absolute; left: 0; right: 0; top: 128px; text-align: center;
    font-size: 44px; font-weight: 400; color: var(--aqua); letter-spacing: .5px;
  }
</style>
</head>
<body>
<main class="canvas">

  <section class="card card-front" aria-label="Card front">
    <div class="front-brand">QVB Consulting</div>

    <div class="holder">
      <div class="holder-name">Miriam Haskett</div>
      <div class="holder-role">Manager</div>
    </div>

    <ul class="contact-list">
      <li class="contact-item">
        <svg class="contact-icon" viewBox="0 0 22 22" aria-hidden="true">
          <rect x="1" y="1" width="20" height="20" rx="3" fill="none" stroke="var(--navy)" stroke-width="1.3"/>
          <rect x="7.5" y="4.5" width="7" height="13" rx="1.2" fill="none" stroke="var(--navy)" stroke-width="1.3"/>
          <rect x="9" y="6.5" width="4" height="5" fill="var(--navy)"/>
          <circle cx="11" cy="15" r=".9" fill="var(--navy)"/>
        </svg>
        <span>0400 386 924</span>
      </li>
      <li class="contact-item">
        <svg class="contact-icon" viewBox="0 0 22 22" aria-hidden="true">
          <rect x="1" y="1" width="20" height="20" rx="3" fill="none" stroke="var(--navy)" stroke-width="1.3"/>
          <rect x="5" y="7" width="12" height="8.5" fill="none" stroke="var(--navy)" stroke-width="1.3"/>
          <path d="M5 7 L11 12 L17 7" fill="none" stroke="var(--navy)" stroke-width="1.3"/>
        </svg>
        <span>miriamrhaskett@fernmail.example</span>
      </li>
      <li class="contact-item">
        <svg class="contact-icon" viewBox="0 0 22 22" aria-hidden="true">
          <rect x="1" y="1" width="20" height="20" rx="3" fill="none" stroke="var(--navy)" stroke-width="1.3"/>
          <path d="M11 18 C8 13.5 6.5 11.5 6.5 9 A4.5 4.5 0 0 1 15.5 9 C15.5 11.5 14 13.5 11 18 Z" fill="var(--navy)"/>
          <circle cx="11" cy="9" r="1.6" fill="#fff"/>
        </svg>
        <span>47 Pallister Crescent,<br>Fernleigh ACT 2699</span>
      </li>
    </ul>

    <div class="edge-band" aria-hidden="true">
      <span class="edge-band-light"></span>
      <span class="edge-band-dark"></span>
    </div>
  </section>

  <section class="card card-back" aria-label="Card back">
    <div class="back-brand">QVB Consulting</div>
  </section>

</main>
</body>
</html>
```